NorthPlain Bytes Yellow rose letterhead

I have a new logo for my company but in its current form it is too large to be used on letterhead or as a email signature. I need to have the designer use elements from the current logo and create something close to the original but more suited for smaller items.
Updates

I just uploaded a copy of our logo that does not have the weathered affect. Thanks

Industry/Entity Type

It Company

Requirements
Must have
• The design must maintain the visual effect of the current logo. It needs to include the yellow rose and the name of the company.
Nice to have
• It would be nice to maintain the stamp theme and incorporate my name, address, phone, email. etc.

```html
<!DOCTYPE html>
<html lang="en">
<head>
<meta charset="utf-8">
<title>NorthPlain Bytes – Stamp Letterhead Mark</title>
<link rel="stylesheet" href="https://fonts.googleapis.com/css2?family=Source+Sans+3:wght@300;400&display=swap">
<style>
  :root {
    --paper: #ffffff;
    --stamp-orange: #f7941d;
    --stamp-glow: #fcc46a;
    --stamp-edge: #5a4b44;
    --panel: #574a43;
    --teal: #35b9bd;
    --olive: #b3b43a;
    --ink-light: #ffffff;
    --rose-light: #fde07a;
    --rose-mid: #f9b933;
    --rose-deep: #f08a1c;
  }
  * { box-sizing: border-box; margin: 0; padding: 0; }
  html, body {
    width: 1200px;
    height: 981px;
    overflow: hidden;
    background: var(--paper);
  }
  .canvas {
    position: relative;
    width: 1200px;
    height: 981px;
    font-family: "Source Sans 3", sans-serif;
  }
  .stamp-frame {
    position: absolute;
    left: 0;
    top: 0;
  }
  .rule {
    position: absolute;
    height: 6px;
    background: var(--teal);
    right: 272px;
  }
  .rule-upper-a { top: 386px; width: 388px; }
  .rule-upper-b { top: 398px; width: 388px; }
  .rule-lower-a { top: 468px; width: 448px; }
  .rule-lower-b { top: 480px; width: 448px; }
  .rose-art {
    position: absolute;
    z-index: 2;
    left: 214px;
    top: 206px;
    width: 326px;
    height: 318px;
    border-radius: 50% 46% 52% 48%;
    background: radial-gradient(circle at 45% 42%, var(--rose-light) 0%, var(--rose-mid) 55%, var(--rose-deep) 100%);
    box-shadow: 12px 14px 0 var(--teal);
  }
  .brand {
    position: absolute;
    right: 272px;
    top: 282px;
    text-align: right;
    font-size: 50px;
    font-weight: 400;
    line-height: 1;
    color: var(--ink-light);
    white-space: nowrap;
  }
  .tagline {
    position: absolute;
    right: 272px;
    top: 412px;
    text-align: right;
    color: var(--olive);
    white-space: nowrap;
  }
  .tagline-title {
    font-size: 26px;
    font-weight: 400;
    letter-spacing: 3px;
  }
  .tagline-sub {
    font-size: 12.5px;
    font-weight: 400;
    letter-spacing: 0.3px;
    margin-top: 2px;
  }
  .contact {
    position: absolute;
    right: 272px;
    top: 500px;
    text-align: right;
    font-style: normal;
    font-weight: 300;
    font-size: 44px;
    line-height: 46px;
    color: var(--ink-light);
    white-space: nowrap;
  }
  .contact .reach { color: var(--teal); }
  .contact .email { margin-top: 18px; }
  .corner-mark {
    position: absolute;
    left: 262px;
    top: 632px;
  }
</style>
</head>
<body>
<main class="canvas">
  <svg class="stamp-frame" width="1200" height="981" viewBox="0 0 1200 981" aria-hidden="true">
    <defs>
      <radialGradient id="stamp-fill" cx="50%" cy="50%" r="60%">
        <stop offset="0%" stop-color="#fcc46a"/>
        <stop offset="70%" stop-color="#f7941d"/>
        <stop offset="100%" stop-color="#f7941d"/>
      </radialGradient>
      <clipPath id="stamp-bounds">
        <rect x="173" y="157" width="854" height="654"/>
      </clipPath>
    </defs>
    <rect x="176" y="160" width="848" height="648" fill="url(#stamp-fill)" stroke="var(--stamp-edge)" stroke-width="5"/>
    <g clip-path="url(#stamp-bounds)" fill="var(--paper)" stroke="var(--stamp-edge)" stroke-width="5">
      <g class="perforations-horizontal">
        <circle cx="211" cy="160" r="24"/><circle cx="282" cy="160" r="24"/><circle cx="353" cy="160" r="24"/>
        <circle cx="423" cy="160" r="24"/><circle cx="494" cy="160" r="24"/><circle cx="565" cy="160" r="24"/>
        <circle cx="635" cy="160" r="24"/><circle cx="706" cy="160" r="24"/><circle cx="777" cy="160" r="24"/>
        <circle cx="847" cy="160" r="24"/><circle cx="918" cy="160" r="24"/><circle cx="989" cy="160" r="24"/>
        <circle cx="211" cy="808" r="24"/><circle cx="282" cy="808" r="24"/><circle cx="353" cy="808" r="24"/>
        <circle cx="423" cy="808" r="24"/><circle cx="494" cy="808" r="24"/><circle cx="565" cy="808" r="24"/>
        <circle cx="635" cy="808" r="24"/><circle cx="706" cy="808" r="24"/><circle cx="777" cy="808" r="24"/>
        <circle cx="847" cy="808" r="24"/><circle cx="918" cy="808" r="24"/><circle cx="989" cy="808" r="24"/>
      </g>
      <g class="perforations-vertical">
        <circle cx="176" cy="196" r="24"/><circle cx="176" cy="268" r="24"/><circle cx="176" cy="340" r="24"/>
        <circle cx="176" cy="412" r="24"/><circle cx="176" cy="484" r="24"/><circle cx="176" cy="556" r="24"/>
        <circle cx="176" cy="628" r="24"/><circle cx="176" cy="700" r="24"/><circle cx="176" cy="772" r="24"/>
        <circle cx="1024" cy="196" r="24"/><circle cx="1024" cy="268" r="24"/><circle cx="1024" cy="340" r="24"/>
        <circle cx="1024" cy="412" r="24"/><circle cx="1024" cy="484" r="24"/><circle cx="1024" cy="556" r="24"/>
        <circle cx="1024" cy="628" r="24"/><circle cx="1024" cy="700" r="24"/><circle cx="1024" cy="772" r="24"/>
      </g>
    </g>
    <rect class="stamp-panel" x="240" y="229" width="728" height="520" fill="var(--panel)"/>
  </svg>

  <div class="rule rule-upper-a"></div>
  <div class="rule rule-upper-b"></div>
  <div class="rule rule-lower-a"></div>
  <div class="rule rule-lower-b"></div>

  <div class="rose-art" role="img" aria-label="Illustration of a yellow rose with dewdrops and a teal shadow"></div>

  <h1 class="brand">NorthPlain Bytes</h1>

  <div class="tagline">
    <p class="tagline-title">THE INSIGHT BUILDERS</p>
    <p class="tagline-sub">Crafting Sharply Focused Consumer Insight for Every Market</p>
  </div>

  <address class="contact">
    <p class="name">Mara Quillen, PhD</p>
    <p class="street">720 NW Red Oak Trail, Ste 4105</p>
    <p class="city">Elm Hollow, TX&nbsp; 76550</p>
    <p class="reach email">mara@northplain-bytes.com</p>
    <p class="reach phone">1.800.555.0148</p>
  </address>

  <svg class="corner-mark" width="92" height="96" viewBox="0 0 92 96" aria-hidden="true">
    <polygon points="0,0 0,96 92,96" fill="var(--teal)"/>
  </svg>
</main>
</body>
</html>
```